Orbit Cheerleading flyer for new recreational cheerleading classes starting in Term 4

I am looking for a flyer to advertise recreational cheerleading classes starting in Term 4. The flyer would need to include the details which are:

For ages 6 -12 years
Monday nights 5pm - 6pm
Starting 10 October 2016

For ages 13 - 18 year
Wednesday nights 7pm - 8pm
Starting 12 October 2016

Classes take place at Unit 4/9 Wexley Lane Mitchell ACT 2905. Cost is $150 for the term

I've attached a copy of a flyer that I really like, the Orbit Cheerleading log and some photos that might be helpful. Our colours are red, black and gold, so I would like those colours incorporated in the flyer please.

Target Market(s)

Girls and boys from 6 years to 18 years

Font styles to use
Sans Serif
Other font styles liked:
• Philly Sans

Colors
f04a50
fece3e
ffffff

Requirements
Must have
• Recreational class details included
• Orbit Logo

```html
<!DOCTYPE html>
<html lang="en">
<head>
<meta charset="utf-8">
<title>Orbit Cheerleading – Recreational Classes Term 4</title>
<link href="https://fonts.googleapis.com/css2?family=Lilita+One&family=Roboto+Condensed:wght@400;700&display=swap" rel="stylesheet">
<style>
  :root {
    --brand-red: #f04a50;
    --brand-gold: #fece3e;
    --white: #ffffff;
    --ink: #231f20;
    --orange-light: #f8923a;
    --orange-mid: #f36a3e;
    --page: #e9e9eb;
  }
  * { margin: 0; padding: 0; box-sizing: border-box; }
  html, body { width: 1200px; height: 856px; overflow: hidden; background: var(--page); }
  body { position: relative; font-family: "Roboto Condensed", Arial, sans-serif; }

  .flyer {
    position: absolute; left: 315px; top: 28px; width: 570px; height: 800px; overflow: hidden;
    background: radial-gradient(ellipse at 50% 38%, var(--orange-light) 0%, var(--orange-mid) 55%, var(--brand-red) 100%);
  }

  .hero-photo {
    position: absolute; left: 25px; top: 0; width: 545px; height: 250px;
    border-radius: 0 0 40px 40px;
    background: linear-gradient(160deg, #c9a33a 0%, #b8322f 45%, #6d1a1c 80%, #d8b548 100%);
    opacity: .9;
  }

  .logo-area {
    position: absolute; left: 125px; top: 236px; width: 320px; height: 130px;
    border-radius: 50%;
    background: radial-gradient(ellipse, #3a1414 0%, #8e2424 60%, rgba(240,74,80,0) 100%);
  }
  .brand-name {
    position: absolute; left: 0; top: 262px; width: 570px; text-align: center;
    font-family: "Lilita One", sans-serif; font-size: 38px; line-height: 38px;
    color: var(--white); text-transform: uppercase; letter-spacing: 1px;
  }

  .headline {
    position: absolute; left: 45px; top: 384px; width: 480px; height: 126px;
    transform: rotate(-8deg); transform-origin: center center;
    font-family: "Lilita One", sans-serif; text-transform: uppercase; font-weight: 400;
  }
  .headline-line {
    display: block; font-size: 52px; line-height: 48px; color: var(--white);
    -webkit-text-stroke: 2px var(--ink); paint-order: stroke fill;
  }
  .headline-sub {
    display: block; margin-left: 28px; font-size: 28px; line-height: 30px; text-transform: none;
    color: var(--brand-gold); -webkit-text-stroke: 1.5px var(--ink); paint-order: stroke fill;
  }
  .term-number {
    position: absolute; left: 448px; top: 410px;
    font-family: "Lilita One", sans-serif; font-size: 115px; line-height: 1;
    color: var(--brand-gold); -webkit-text-stroke: 3px var(--ink); paint-order: stroke fill;
    transform: rotate(-8deg);
  }

  .session {
    position: absolute; top: 555px; width: 240px; text-align: center; color: var(--white);
  }
  .session--junior { left: 5px; }
  .session--senior { left: 317px; }
  .session-age { font-size: 21px; font-weight: 700; line-height: 25px; }
  .session-label { font-size: 14px; font-weight: 700; color: var(--brand-gold); text-transform: uppercase; line-height: 20px; }
  .session-value { font-size: 18px; font-weight: 700; line-height: 22px; }

  .price-badge { position: absolute; left: 237px; top: 598px; width: 96px; height: 96px; }
  .price-text {
    position: absolute; left: 237px; top: 614px; width: 96px; text-align: center;
    font-weight: 700; color: var(--white);
  }
  .price-label { font-size: 18px; line-height: 22px; }
  .price-amount { font-size: 30px; line-height: 32px; color: var(--brand-gold); }

  .price-ribbon { position: absolute; left: 178px; top: 684px; width: 212px; height: 28px; }
  .price-ribbon-text {
    position: absolute; left: 178px; top: 684px; width: 212px; line-height: 28px; text-align: center;
    font-size: 18px; color: var(--ink); text-transform: uppercase;
  }

  .venue {
    position: absolute; left: 0; top: 724px; width: 570px; height: 76px;
    background: var(--brand-red); border-top: 3px solid var(--brand-gold);
    text-align: center;
  }
  .venue-label { margin-top: 13px; font-size: 12px; line-height: 15px; color: var(--ink); text-transform: uppercase; }
  .venue-address { font-size: 22px; font-weight: 700; line-height: 28px; color: var(--white); }
</style>
</head>
<body>
  <main class="flyer">
    <div class="hero-photo" role="img" aria-label="Photo of a young cheerleader in team uniform jumping with gold pom-poms"></div>

    <div class="logo-area" role="img" aria-label="Dark burst backdrop for the club name"></div>
    <div class="brand-name">Orbit<br>Cheerleading</div>

    <h1 class="headline">
      <span class="headline-line">Recreational</span>
      <span class="headline-line">Cheerleading</span>
      <span class="headline-sub">Classes Starting In Term</span>
    </h1>
    <div class="term-number">4</div>

    <section class="session session--junior">
      <p class="session-age">For Ages 6 -12 Years</p>
      <p class="session-label">Monday Nights</p>
      <p class="session-value">5pm - 6pm</p>
      <p class="session-label">Starting</p>
      <p class="session-value">10 October 2016</p>
    </section>

    <section class="session session--senior">
      <p class="session-age">For Ages 13 -18 Years</p>
      <p class="session-label">Wednesday Nights</p>
      <p class="session-value">7pm - 8pm</p>
      <p class="session-label">Starting</p>
      <p class="session-value">12 October 2016</p>
    </section>

    <svg class="price-badge" viewBox="0 0 84 84" aria-hidden="true">
      <polygon fill="#231f20" points="42,0 49,10 60,4 62,16 75,15 71,27 83,33 74,42 83,51 71,57 75,69 62,68 60,80 49,74 42,84 35,74 24,80 22,68 9,69 13,57 1,51 10,42 1,33 13,27 9,15 22,16 24,4 35,10"/>
    </svg>
    <div class="price-text">
      <p class="price-label">COST</p>
      <p class="price-amount">$150</p>
    </div>

    <svg class="price-ribbon" viewBox="0 0 212 28" aria-hidden="true">
      <polygon fill="#fece3e" points="0,2 16,2 16,26 0,26 8,14"/>
      <polygon fill="#fece3e" points="212,2 196,2 196,26 212,26 204,14"/>
      <rect x="12" y="0" width="188" height="28" fill="#fece3e"/>
    </svg>
    <div class="price-ribbon-text">For The Term</div>

    <footer class="venue">
      <p class="venue-label">Classes take place at unit</p>
      <p class="venue-address">4/9 Wexley Lane Mitchell ACT 2905.</p>
    </footer>
  </main>
</body>
</html>
```